Looking for a clean, modern, and professional business card design that reflects Valtrim Systems

The design should include the company logo, contact details, and align with our brand identity. Please use a sophisticated and minimalist style, incorporating [specific colors, if applicable]. Creativity is welcome, but the card must maintain a polished and professional appearance.

Details to Include:

Name: Gavin Trelowe
Title: VP Sales / Operations
Company: Valtrim Systems
Phone: 483.216.7705
Email: gavin@valtrimsystems-example.com
Website: www.valtrimsystems-example.com

```html
<!DOCTYPE html>
<html lang="en">
<head>
<meta charset="utf-8">
<title>Valtrim Systems — Business Card</title>
<link rel="stylesheet" href="https://fonts.googleapis.com/css2?family=Montserrat:wght@400;600;700&family=Roboto:wght@400;700&display=swap">
<style>
  :root {
    --stage: #e9ebee;
    --card-white: #fdfdfd;
    --ink: #1b1b1d;
    --ink-soft: #3a3a3d;
    --brand-blue: #3f82c9;
    --blue-deep: #1f55a3;
    --blue-light: #3f7fc0;
    --emboss: #f1f2f3;
    --emboss-edge: #e3e5e8;
  }
  * { box-sizing: border-box; margin: 0; padding: 0; }
  html, body { width: 1200px; height: 900px; overflow: hidden; }
  body {
    background: var(--stage);
    display: flex;
    flex-direction: column;
    align-items: center;
    justify-content: center;
    gap: 56px;
    font-family: "Roboto", Arial, sans-serif;
  }
  .card {
    width: 620px;
    height: 354px;
    border-radius: 4px;
    position: relative;
    overflow: hidden;
    box-shadow: 0 10px 28px rgba(20, 30, 50, 0.18);
  }

  /* Front */
  .card--front { background: var(--card-white); }
  .front__brand {
    position: absolute;
    left: 44px;
    top: 46px;
    font-family: "Montserrat", Arial, sans-serif;
    font-weight: 700;
    font-size: 30px;
    letter-spacing: 1px;
    color: var(--ink);
    text-transform: uppercase;
  }
  .front__person { position: absolute; left: 44px; top: 136px; }
  .person__name {
    font-weight: 700;
    font-size: 19px;
    color: var(--ink);
    text-transform: uppercase;
    letter-spacing: 0.2px;
  }
  .person__title {
    margin-top: 3px;
    font-size: 16px;
    color: var(--brand-blue);
  }
  .contact-list {
    list-style: none;
    position: absolute;
    left: 44px;
    top: 210px;
    display: flex;
    flex-direction: column;
    gap: 7px;
  }
  .contact-list__item {
    display: flex;
    align-items: center;
    gap: 9px;
    font-size: 15px;
    color: var(--ink-soft);
  }
  .contact-list__icon { width: 15px; height: 15px; flex: none; }
  .front__emboss {
    position: absolute;
    right: 34px;
    top: 70px;
    width: 230px;
    height: 230px;
    border-radius: 6px;
    background: linear-gradient(135deg, var(--emboss) 0%, var(--emboss-edge) 100%);
  }

  /* Back */
  .card--back {
    background: linear-gradient(160deg, var(--blue-light) 0%, var(--blue-deep) 100%);
    display: flex;
    flex-direction: column;
    align-items: center;
    justify-content: center;
    gap: 22px;
  }
  .back__brand {
    font-family: "Montserrat", Arial, sans-serif;
    font-weight: 700;
    font-size: 44px;
    letter-spacing: 2px;
    color: #ffffff;
    text-transform: uppercase;
  }
  .back__tagline {
    font-family: "Montserrat", Arial, sans-serif;
    font-weight: 400;
    font-size: 14px;
    letter-spacing: 5px;
    color: rgba(255, 255, 255, 0.85);
    text-transform: uppercase;
  }
</style>
</head>
<body>
  <section class="card card--front">
    <div class="front__brand">Valtrim Systems</div>
    <div class="front__person">
      <p class="person__name">Gavin Trelowe</p>
      <p class="person__title">VP Sales / Operations</p>
    </div>
    <ul class="contact-list">
      <li class="contact-list__item">
        <svg class="contact-list__icon" viewBox="0 0 16 16" aria-hidden="true">
          <path fill="#3f82c9" d="M3.5 1.5l2.3 2.6-1.2 1.7c.8 1.9 2.2 3.3 4.1 4.1l1.7-1.2 2.6 2.3-1.3 2.3C6.8 13.3 2.7 9.2 1.2 4.3z"/>
        </svg>
        483.216.7705
      </li>
      <li class="contact-list__item">
        <svg class="contact-list__icon" viewBox="0 0 16 16" aria-hidden="true">
          <rect x="1" y="3" width="14" height="10" rx="1" fill="#3f82c9"/>
          <path d="M1.5 4l6.5 5 6.5-5" fill="none" stroke="#fff" stroke-width="1.2"/>
        </svg>
        gavin@valtrimsystems-example.com
      </li>
      <li class="contact-list__item">
        <svg class="contact-list__icon" viewBox="0 0 16 16" aria-hidden="true">
          <circle cx="8" cy="8" r="7" fill="#3f82c9"/>
          <path d="M1 8h14M8 1c2.5 2.5 2.5 11.5 0 14M8 1c-2.5 2.5-2.5 11.5 0 14" fill="none" stroke="#fff" stroke-width="0.9"/>
        </svg>
        www.valtrimsystems-example.com
      </li>
    </ul>
    <div class="front__emboss" role="img" aria-label="Blind-embossed brand symbol"></div>
  </section>

  <section class="card card--back">
    <div class="back__brand">Valtrim Systems</div>
    <p class="back__tagline">Valtrim Systems</p>
  </section>
</body>
</html>
```